KGDB Business Card

Looking for a business card design to incorporate our branding. We want to only use the colors listing in the Branding Package (attached).
Updates

Target Market(s)

People who need their phone or device fixed.

Industry/Entity Type

Electronics

Contact Information for Business Card

Please use:

Bright Circuit Mending Depot LLC
3478 S Ridge Trail 2210 E
Suite 417
San Antonio, TX 78341

Marcus Delwyn, Store Manager

(210) 555-0143

Requirements
Must have
• Must include the colors that are contained within the Branding Package PDF file.

```html
<!DOCTYPE html>
<html lang="en">
<head>
<meta charset="utf-8">
<title>KGDB Business Card</title>
<link rel="stylesheet" href="https://fonts.googleapis.com/css2?family=Open+Sans:wght@400;600;700&display=swap">
<style>
  :root {
    --brand-orange: #e04e1f;
    --brand-orange-dark: #d2441a;
    --brand-lime: #c4c84a;
    --paper: #f7f7f7;
    --ink: #5a5a5a;
    --stage: #d9d9d9;
    --faint-orange: rgba(224, 78, 31, 0.28);
    --faint-ink: rgba(90, 90, 90, 0.28);
  }
  * { box-sizing: border-box; margin: 0; padding: 0; }
  html, body {
    width: 1200px;
    height: 904px;
    overflow: hidden;
    background: var(--stage);
    font-family: "Open Sans", sans-serif;
  }
  .sheet {
    width: 1200px;
    height: 904px;
    display: flex;
    flex-direction: column;
    align-items: center;
    justify-content: center;
    gap: 56px;
  }
  .card {
    position: relative;
    width: 580px;
    height: 330px;
    border-radius: 20px;
    overflow: hidden;
    box-shadow: 0 6px 18px rgba(0, 0, 0, 0.18);
  }
  /* Back side */
  .card--back {
    background: linear-gradient(135deg, var(--brand-orange) 0%, var(--brand-orange-dark) 100%);
    display: flex;
    align-items: center;
    justify-content: center;
    gap: 16px;
  }
  .back-mark {
    width: 46px;
    height: 46px;
    border-radius: 10px;
    background: var(--brand-lime);
  }
  .back-name {
    font-size: 44px;
    font-weight: 600;
    color: #ffffff;
    letter-spacing: 2px;
  }
  /* Front side */
  .card--front {
    background: linear-gradient(160deg, #ffffff 0%, var(--paper) 100%);
  }
  .brand {
    position: absolute;
    left: 40px;
    top: 42px;
    display: flex;
    align-items: center;
    gap: 12px;
  }
  .brand-square {
    width: 42px;
    height: 42px;
    border-radius: 9px;
    background: var(--brand-orange);
  }
  .brand-name {
    font-size: 34px;
    font-weight: 600;
    color: var(--brand-orange);
    letter-spacing: 1px;
  }
  .details {
    position: absolute;
    left: 120px;
    top: 128px;
    color: var(--ink);
    font-size: 14px;
    line-height: 1.45;
  }
  .person-name {
    font-size: 21px;
    font-weight: 700;
    color: var(--brand-orange);
    line-height: 1.2;
  }
  .person-role { margin-bottom: 4px; }
  .phone {
    display: flex;
    align-items: center;
    gap: 8px;
    margin-bottom: 8px;
  }
  .phone svg { width: 11px; height: 17px; }
  .company {
    color: var(--brand-orange);
    font-size: 14.5px;
  }
  .faint-brand {
    position: absolute;
    right: -40px;
    top: 60px;
    width: 230px;
  }
  .faint-name {
    font-size: 50px;
    font-weight: 600;
    color: var(--faint-ink);
    letter-spacing: 2px;
    line-height: 1;
    margin-bottom: 10px;
  }
  .faint-square {
    width: 200px;
    height: 200px;
    border-radius: 34px;
    background: var(--faint-orange);
  }
</style>
</head>
<body>
<main class="sheet">
  <section class="card card--back" aria-label="Card back">
    <div class="back-mark"></div>
    <div class="back-name">KGDB</div>
  </section>

  <section class="card card--front" aria-label="Card front">
    <div class="faint-brand" aria-hidden="true">
      <div class="faint-name">KGDB</div>
      <div class="faint-square"></div>
    </div>

    <div class="brand">
      <div class="brand-square"></div>
      <div class="brand-name">KGDB</div>
    </div>

    <div class="details">
      <div class="person-name">Marcus Delwyn</div>
      <div class="person-role">Store Manager</div>
      <div class="phone">
        <svg viewBox="0 0 11 17" aria-hidden="true">
          <rect x="1" y="1" width="9" height="15" rx="1.5" fill="none" stroke="#e04e1f" stroke-width="1.4"/>
          <line x1="4" y1="13.2" x2="7" y2="13.2" stroke="#e04e1f" stroke-width="1.2"/>
        </svg>
        <span>(210) 555-0143</span>
      </div>
      <div class="company">Bright Circuit Mending Depot LLC</div>
      <div>3478 S Ridge Trail 2210 E</div>
      <div>Suite 417</div>
      <div>San Antonio, TX 78341</div>
    </div>
  </section>
</main>
</body>
</html>
```